Vornel Technologies business card design

We need a business card designed with our new logo. it would be great if the card could communicate it is a technology based company.

Target Market(s)

system integrators

Industry/Entity Type

technology, IOT

Contact Information for Business Card

Name, designation, Address, telephone number, email address

Requirements
Must have
• logo and company name
Nice to have
• something to do with technology

```html
<!DOCTYPE html>
<html lang="en">
<head>
<meta charset="utf-8">
<title>Vornel Technologies – Business Card</title>
<link href="https://fonts.googleapis.com/css2?family=Raleway:wght@600;700&family=Noto+Sans:wght@400&display=swap" rel="stylesheet">
<style>
  :root {
    --ink: #000000;
    --paper: #ffffff;
    --accent: #f7941d;
    --shadow-line: #1e1e1e;
  }
  html, body {
    margin: 0;
    padding: 0;
    width: 868px;
    height: 1200px;
    overflow: hidden;
    background: var(--paper);
  }
  .canvas {
    position: relative;
    width: 868px;
    height: 1200px;
    background: var(--paper);
  }
  .card {
    position: absolute;
    left: 0;
    width: 868px;
    background: var(--ink);
    overflow: hidden;
  }
  .card--front { top: 0; height: 567px; }
  .card--back { top: 630px; height: 570px; }
  .card svg.frame { position: absolute; inset: 0; }

  .brand {
    position: absolute;
    font-family: "Raleway", sans-serif;
    font-weight: 700;
    color: var(--paper);
    margin: 0;
    line-height: 1.05;
  }
  .brand--front {
    left: 22px;
    top: 78px;
    font-size: 44px;
    letter-spacing: 1px;
  }
  .brand--back {
    left: 0;
    width: 868px;
    top: 225px;
    text-align: center;
    font-size: 52px;
    letter-spacing: 1px;
  }
  .brand-square {
    display: inline-block;
    width: 26px;
    height: 26px;
    background: var(--accent);
    margin-right: 16px;
    vertical-align: 4px;
  }

  .person {
    position: absolute;
    left: 380px;
    width: 446px;
    top: 36px;
    text-align: center;
    font-family: "Raleway", sans-serif;
  }
  .person__name {
    margin: 0;
    color: var(--paper);
    font-weight: 700;
    font-size: 62px;
    line-height: 1;
  }
  .person__role {
    margin: 12px 0 0;
    color: var(--accent);
    font-weight: 600;
    font-size: 26px;
    letter-spacing: 0.5px;
  }

  .contacts {
    position: absolute;
    left: 344px;
    top: 314px;
    margin: 0;
    padding: 0;
    list-style: none;
    font-family: "Noto Sans", sans-serif;
    font-size: 25px;
    color: var(--paper);
    letter-spacing: 0.5px;
  }
  .contacts li {
    display: flex;
    align-items: center;
    height: 36px;
    margin-bottom: 24px;
  }
  .contacts li:last-child { margin-bottom: 0; }
  .contacts svg { width: 32px; height: 32px; margin-right: 27px; flex: none; }

  .website {
    position: absolute;
    left: 0;
    width: 868px;
    top: 494px;
    text-align: center;
    font-family: "Noto Sans", sans-serif;
    font-size: 25px;
    letter-spacing: 1px;
    color: var(--paper);
  }
</style>
</head>
<body>
<div class="canvas">

  <section class="card card--front">
    <svg class="frame" width="868" height="567" viewBox="0 0 868 567" aria-hidden="true">
      <polyline points="0,419 144,419 387,176 868,176" fill="none" stroke="var(--shadow-line)" stroke-width="9"/>
      <polyline points="0,410 140,410 383,164 868,164" fill="none" stroke="var(--accent)" stroke-width="9"/>
    </svg>

    <p class="brand brand--front">Vornel<br>Technologies</p>

    <header class="person">
      <h1 class="person__name">YOUR NAME</h1>
      <p class="person__role">DESIGNATION</p>
    </header>

    <ul class="contacts">
      <li>
        <svg viewBox="0 0 32 32" aria-hidden="true">
          <circle cx="16" cy="16" r="13.5" fill="none" stroke="var(--accent)" stroke-width="3"/>
          <path d="M11 9.5c1-1 2-1 2.6 0l1.4 2.4c.4.8.2 1.4-.5 2l-1 .8c.8 1.8 2 3 3.8 3.8l.8-1c.6-.7 1.2-.9 2-.5l2.4 1.4c1 .6 1 1.6 0 2.6-1.4 1.4-3 1.6-5 .6-3-1.5-5.1-3.6-6.6-6.6-1-2-.8-3.6.1-5.5z" fill="var(--accent)"/>
        </svg>
        <span>+12 3456 78 90</span>
      </li>
      <li>
        <svg viewBox="0 0 32 32" aria-hidden="true">
          <path d="M16 2c-6 0-10.5 4.5-10.5 10.2C5.5 19 16 30 16 30s10.5-11 10.5-17.8C26.5 6.5 22 2 16 2z" fill="var(--accent)"/>
          <circle cx="16" cy="12.2" r="4.6" fill="var(--ink)"/>
        </svg>
        <span>Your Address XYZ</span>
      </li>
      <li>
        <svg viewBox="0 0 32 32" aria-hidden="true">
          <rect x="1" y="6" width="30" height="20" fill="var(--accent)"/>
          <polyline points="2,7.5 16,18 30,7.5" fill="none" stroke="var(--ink)" stroke-width="2"/>
          <polyline points="2,25 12,15.5 M30,25 20,15.5" fill="none" stroke="var(--ink)" stroke-width="2"/>
          <line x1="2" y1="25" x2="12" y2="15.5" stroke="var(--ink)" stroke-width="2"/>
          <line x1="30" y1="25" x2="20" y2="15.5" stroke="var(--ink)" stroke-width="2"/>
        </svg>
        <span>info@mail.com</span>
      </li>
    </ul>
  </section>

  <section class="card card--back">
    <svg class="frame" width="868" height="570" viewBox="0 0 868 570" aria-hidden="true">
      <polyline points="0,410 177,410 212,444 655,444 690,410 868,410" fill="none" stroke="var(--shadow-line)" stroke-width="9"/>
      <polyline points="0,419 171,419 205,455 662,455 696,419 868,419" fill="none" stroke="var(--accent)" stroke-width="9"/>
    </svg>

    <p class="brand brand--back"><span class="brand-square" aria-hidden="true"></span>Vornel Technologies</p>

    <p class="website">www.website.com</p>
  </section>

</div>
</body>
</html>
```